My Billboard for Law Firm

Designing a billboard

Should have
Corvell & Pine, LLC
Ph: 555-214-7390
Auto Accidents / Personal Injury
Family Law
Criminal Defense
Real Estate
Free Consultation

Target Market(s)

Legal

Industry/Entity Type

Legal

Font styles to use
Serif
Sans Serif

Requirements
Must have
• Designing a billboard

Should have
Corvell & Pine, LLC
Ph: 555-214-7390
Family Law
Criminal Defense
Real Estate
Free Consultation
Nice to have
• Nice to have info above
Should not have
• None

```html
<!DOCTYPE html>
<html lang="en">
<head>
<meta charset="utf-8">
<title>Corvell &amp; Pine, LLC — Billboard</title>
<link href="https://fonts.googleapis.com/css2?family=Tinos:wght@700&display=swap" rel="stylesheet">
<style>
  :root {
    --page-bg: #e9ebef;
    --panel-dark: #2a211f;
    --strip-warm: #7b3c3d;
    --strip-cool: #5b4f55;
    --photo-warm: #6a4344;
    --photo-mid: #4a4247;
    --photo-deep: #2c2c33;
    --bronze: #8a7558;
    --text-light: #f4f2ef;
  }
  * { margin: 0; padding: 0; box-sizing: border-box; }
  html, body {
    width: 1200px;
    height: 800px;
    overflow: hidden;
    background: var(--page-bg);
  }
  .billboard {
    position: absolute;
    left: 50px;
    top: 100px;
    width: 1100px;
    height: 600px;
    overflow: hidden;
    font-family: "Tinos", "Times New Roman", serif;
    font-weight: 700;
    color: var(--text-light);
  }
  .billboard-shapes {
    position: absolute;
    inset: 0;
    width: 100%;
    height: 100%;
  }
  .firm-name {
    position: absolute;
    left: 95px;
    top: 52px;
    font-size: 38px;
    letter-spacing: 0.5px;
  }
  .practice-list {
    position: absolute;
    left: 150px;
    top: 190px;
    list-style: none;
    font-size: 37px;
    line-height: 42px;
    letter-spacing: 0.5px;
  }
  .phone {
    position: absolute;
    left: 118px;
    top: 488px;
    font-size: 64px;
    letter-spacing: 0.5px;
  }
</style>
</head>
<body>
  <main class="billboard">
    <svg class="billboard-shapes" viewBox="0 0 1100 600" preserveAspectRatio="none" aria-hidden="false">
      <defs>
        <linearGradient id="side-strip" x1="0" y1="0" x2="0.4" y2="1">
          <stop offset="0" stop-color="var(--strip-warm)"/>
          <stop offset="0.6" stop-color="#6d4447"/>
          <stop offset="1" stop-color="var(--strip-cool)"/>
        </linearGradient>
        <linearGradient id="statue-tones" x1="0" y1="0" x2="1" y2="1">
          <stop offset="0" stop-color="var(--photo-warm)"/>
          <stop offset="0.35" stop-color="var(--bronze)"/>
          <stop offset="0.6" stop-color="var(--photo-mid)"/>
          <stop offset="1" stop-color="var(--photo-deep)"/>
        </linearGradient>
      </defs>
      <rect class="side-strip" x="0" y="0" width="1100" height="600" fill="url(#side-strip)"/>
      <polygon class="statue-photo" points="470,0 1100,0 1100,600 525,600"
               fill="url(#statue-tones)" role="img"
               aria-label="Photograph of a bronze Lady Justice statue holding the scales of justice"/>
      <polygon class="text-panel" points="62,0 472,0 527,600 108,600" fill="var(--panel-dark)"/>
    </svg>

    <h1 class="firm-name">Corvell &amp; Pine, LLC</h1>
    <ul class="practice-list">
      <li>Auto Accidents</li>
      <li>Personal Injury</li>
      <li>Family Law</li>
      <li>Criminal Defense</li>
      <li>Real Estate</li>
      <li>Free Consultation</li>
    </ul>
    <p class="phone">555-214-7390</p>
  </main>
</body>
</html>
```